Hiking Made Simple Outfitter Directory

Hero Section
Image: A serene and picturesque camping landscape with a lake, mountains, and a few trees There is a circle of people sitting around a campfire. The image should be high-quality and visually appealing.
Headline: "Introducing Hikingmadesimple.net's Outfitter Directory"
Subheading: "Join our directory of trusted outfitters and reach a targeted audience of camping enthusiasts."
Call-to-Action (CTA) Button: "Learn More" or "Join Now"
Color scheme: Match hikingmadesimple.net and the logo
Example:
[Image: A serene and picturesque camping landscape with a lake, mountains, and a few trees]
Introducing Hikingmadesimple.net's Outfitter Directory
Join our directory of trusted outfitters and reach a targeted audience of camping enthusiasts.
Learn More
Benefits Section
Image: A group of happy campers sitting around a campfire, roasting marshmallows and telling stories.
Headline: "Benefits of Joining Our Directory"
Bullet points:
"Increase your exposure and visibility to potential customers"
"Book more trips and generate more revenue"
"Access a targeted audience of camping enthusiasts"
Color scheme: match hikingmadesimple.net
Example:
[Image: A group of happy campers sitting around a campfire, roasting marshmallows and telling stories]
Benefits of Joining Our Directory
• Increase your exposure and visibility to potential customers • Book more trips and generate more revenue • Access a targeted audience of camping enthusiasts
Features Section
Image: A screenshot of the directory's search functionality, showing a list of outfitters with their logos, names, and locations.
Headline: "Features of Our Outfitter Directory"
Bullet points:
"Search functionality to find outfitters by location, activity, or type"
"Outfitter profiles with detailed information and reviews"
"Booking system to make it easy for customers to book trips"
Example:
[Image: A screenshot of the directory's search functionality, showing a list of outfitters with their logos, names, and locations]
Features of Our Outfitter Directory
• Search functionality to find outfitters by location, activity, or type • Outfitter profiles with detailed information and reviews • Booking system to make it easy for customers to book trips
CTA Section
Image: A simple and clean design with a prominent call-to-action button.
Headline: "Express Interest in Joining Our Directory"
Call-to-Action (CTA) Button: "Express Interest" or "Join Now"

Example:
[Image: A simple and clean design with a prominent call-to-action button]
Express Interest in Joining Our Directory
Express Interest
Contact Information Section
Image: A simple and clean design with a form to collect contact information.
Headline: "Get in Touch with Us"
Form fields:
Name
Email
Phone
Website

```html
<!DOCTYPE html>
<html lang="en">
<head>
<meta charset="utf-8">
<title>Hiking Made Simple – Outfitter Directory</title>
<link rel="stylesheet" href="https://fonts.googleapis.com/css2?family=Bebas+Neue&family=Caveat:wght@600&family=Poppins:wght@400;500;600;700&display=swap">
<style>
:root{
  --orange:#f65a1c;
  --orange-dark:#e2470f;
  --ink:#121212;
  --body:#3d3d3d;
  --teal:#14a39a;
  --phone:#0d8fa0;
  --beige:#f3e9e1;
  --navy:#0f2447;
  --line:#d9d9d9;
  --white:#ffffff;
}
*{box-sizing:border-box;margin:0;padding:0}
html,body{width:1200px;height:3522px;overflow:hidden;background:var(--white)}
body{font-family:"Poppins",sans-serif;color:var(--ink);position:relative}
.abs{position:absolute}

/* header */
.site-header{position:absolute;left:0;top:0;width:1200px;height:98px;background:var(--white)}
.brand{position:absolute;left:142px;top:22px;display:flex;align-items:center;gap:8px}
.brand-dot{width:14px;height:14px;border-radius:50%;background:var(--orange)}
.brand-name{font-weight:700;font-size:15px;line-height:17px;color:var(--navy);width:80px}
.header-contact{position:absolute;top:32px;display:flex;align-items:center;gap:12px}
.icon-badge{width:32px;height:32px;border-radius:50%;background:var(--orange);display:flex;align-items:center;justify-content:center}
.header-contact .label{font-size:10.5px;font-weight:600;color:var(--ink);line-height:14px}
.header-contact .value{font-size:11px;color:#666;line-height:15px}
.header-contact .value.phone{color:var(--phone);font-weight:500}
.header-divider{position:absolute;left:1022px;top:30px;width:1px;height:38px;background:var(--line)}
.search-btn{position:absolute;left:1043px;top:40px}

/* hero */
.hero{position:absolute;left:0;top:98px;width:1200px;height:695px;overflow:hidden}
.hero-photo{position:absolute;inset:0;background:
  radial-gradient(ellipse 380px 200px at 600px 330px,rgba(248,176,40,.55),rgba(248,176,40,0) 70%),
  radial-gradient(ellipse 700px 260px at 600px 330px,rgba(238,150,80,.55),rgba(0,0,0,0) 75%),
  linear-gradient(180deg,#6d6563 0%,#8a7464 28%,#c27a4a 45%,#6c4a33 62%,#3d2a1e 100%)}
.hero-edge{position:absolute;left:0;bottom:0;width:1200px;height:60px}
.hero-script{position:absolute;left:0;width:1200px;top:150px;text-align:center;font-family:"Caveat",cursive;font-size:34px;color:var(--white)}
.hero-title{position:absolute;left:0;width:1200px;top:188px;text-align:center;font-family:"Bebas Neue",sans-serif;font-size:92px;line-height:84px;color:var(--white);letter-spacing:2px}
.hero-sub{position:absolute;left:0;width:1200px;top:374px;text-align:center;font-size:13.5px;font-weight:500;color:var(--white)}
.hero-cta{position:absolute;left:525px;top:423px;width:149px;height:41px;background:var(--orange);color:var(--white);font-size:12px;font-weight:600;letter-spacing:1px;display:flex;align-items:center;justify-content:center}
.slider-nav{position:absolute;top:290px;display:flex;align-items:center;color:var(--white);font-size:14px}
.slider-nav .ring{width:42px;height:42px;border:1.5px solid var(--white);border-radius:50%}
.slider-nav .rule{width:42px;height:1px;background:rgba(255,255,255,.8)}
.slider-nav .dot{width:5px;height:5px;border-radius:50%;background:var(--white)}

/* shared */
.eyebrow{font-size:13px;color:var(--orange);display:flex;align-items:center;gap:8px}
.eyebrow .dash{width:50px;height:1px;background:var(--orange)}
.section-title{font-weight:700;font-size:33px;line-height:40px;color:var(--ink);text-transform:uppercase;letter-spacing:-.3px}
.para{font-size:13.5px;line-height:23px;color:var(--body)}
.pill{height:38px;border-radius:19px;background:var(--orange);color:var(--white);font-size:13px;display:flex;align-items:center;justify-content:center}
.photo{border-radius:8px;overflow:hidden}
.photo-framed{border:5px solid var(--white);border-radius:4px}

/* benefits */
.benefits-list{list-style:none}
.benefits-list li{display:flex;align-items:center;gap:8px;font-size:13px;font-weight:500;color:var(--ink);height:29px}
.tick{width:14px;height:14px;border-radius:50%;background:var(--teal);display:flex;align-items:center;justify-content:center}

/* features */
.features{position:absolute;left:0;top:1386px;width:1200px;height:767px;background:var(--beige)}
.feature{position:absolute;width:280px;text-align:center}
.feature-icon{display:block;margin:0 auto}
.feature-text{margin-top:36px;font-size:17.5px;line-height:25px;font-weight:500;color:var(--ink)}

/* contact form */
.field{position:absolute;left:636px;width:309px;height:41px;border:1px solid var(--line);display:flex;align-items:center;background:var(--white)}
.field .fi{width:40px;height:100%;border-right:1px solid var(--line);display:flex;align-items:center;justify-content:center}
.field span{padding-left:11px;font-size:13px;color:#555}
.field b{color:var(--orange);font-weight:500}

/* cta band */
.cta-band{position:absolute;left:0;top:2778px;width:1200px;height:373px;overflow:hidden}
.cta-title{position:absolute;left:144px;top:124px;font-weight:700;font-size:31px;line-height:40px;color:var(--white);text-transform:uppercase}

/* footer */
.footer-head{font-weight:600;font-size:15.5px;color:var(--ink)}
.footer-item{position:absolute;display:flex;align-items:center;gap:12px;font-size:13px;color:var(--ink);line-height:16px}
.ring-icon{width:37px;height:37px;border-radius:50%;background:var(--orange);border:3px solid #fbd2c0;display:flex;align-items:center;justify-content:center;flex:none}
.social-dot{width:10px;height:10px;border-radius:50%;background:var(--white)}
.copyright{position:absolute;left:0;top:3479px;width:1200px;height:43px;background:var(--navy);color:#e6e9ef;font-size:13px;display:flex;align-items:center;justify-content:center}
</style>
</head>
<body>

<header class="site-header">
  <div class="brand"><span class="brand-dot"></span><span class="brand-name">Hiking Made Simple</span></div>
  <div class="header-contact" style="left:644px">
    <div class="icon-badge"><svg width="14" height="11" viewBox="0 0 14 11"><rect x="0.5" y="0.5" width="13" height="10" rx="1.5" fill="#fff"/><path d="M1 1.5l6 4.5 6-4.5" stroke="#f65a1c" stroke-width="1.3" fill="none"/></svg></div>
    <div><div class="label">Email Us</div><div class="value">info@hikingmadesimple.net</div></div>
  </div>
  <div class="header-contact" style="left:867px">
    <div class="icon-badge"><svg width="14" height="14" viewBox="0 0 24 24"><path fill="#fff" d="M6.6 10.8a15 15 0 0 0 6.6 6.6l2.2-2.2c.3-.3.7-.4 1-.2 1.1.4 2.3.6 3.6.6.6 0 1 .4 1 1V20c0 .6-.4 1-1 1A17 17 0 0 1 3 4c0-.6.4-1 1-1h3.5c.6 0 1 .4 1 1 0 1.3.2 2.5.6 3.6.1.3 0 .7-.2 1z"/></svg></div>
    <div><div class="label">Call Anytime</div><div class="value phone">(555) 410-2276</div></div>
  </div>
  <div class="header-divider"></div>
  <svg class="search-btn" width="17" height="17" viewBox="0 0 17 17"><circle cx="7" cy="7" r="5.8" stroke="#333" stroke-width="1.4" fill="none"/><path d="M11.3 11.3l4.5 4.5" stroke="#333" stroke-width="1.4"/></svg>
</header>

<section class="hero">
  <div class="hero-photo" role="img" aria-label="View from inside an open tent of a camper watching a forested mountain valley at sunset"></div>
  <div class="hero-script">Fun For The Whole Family</div>
  <h1 class="hero-title">Camping With<br>Family Gives Joy</h1>
  <p class="hero-sub">Join our directory of trusted outfitters and reach a targeted audience of camping enthusiasts.</p>
  <div class="hero-cta">JOIN NOW</div>
  <div class="slider-nav" style="left:30px"><div class="ring"></div><span style="margin-left:-15px;margin-right:10px">Prev</span><span class="dot"></span><span class="rule"></span></div>
  <div class="slider-nav" style="left:1059px"><span class="rule"></span><span class="dot"></span><span style="margin-left:10px;margin-right:-15px">Next</span><div class="ring"></div></div>
  <svg class="hero-edge" viewBox="0 0 1200 60" preserveAspectRatio="none"><path d="M0 40 Q300 20 600 38 T1200 34 V60 H0 Z" fill="#fff"/></svg>
</section>

<section class="benefits">
  <div class="eyebrow abs" style="left:141px;top:886px">Our Benefits <span class="dash"></span></div>
  <h2 class="section-title abs" style="left:140px;top:900px;width:460px">Benefits of Joining Our Directory</h2>
  <p class="para abs" style="left:141px;top:990px;width:440px">Lorem ipsum dolor sit amet, consectetur adipiscing elit, sed do sit em eiusmod tempor incididunt ut labore et dolore magna aliqua. Ut enim ad minim veniam, quis nostrud exercitation ullamco laboris nisi ut aliquip ex ea commodo consequat.</p>
  <ul class="benefits-list abs" style="left:141px;top:1089px">
    <li><span class="tick"><svg width="8" height="8" viewBox="0 0 8 8"><path d="M1 4l2 2 4-4.5" stroke="#fff" stroke-width="1.5" fill="none"/></svg></span>Increase your exposure and visibility to potential customers</li>
    <li><span class="tick"><svg width="8" height="8" viewBox="0 0 8 8"><path d="M1 4l2 2 4-4.5" stroke="#fff" stroke-width="1.5" fill="none"/></svg></span>Book more trips and generate more revenue</li>
    <li><span class="tick"><svg width="8" height="8" viewBox="0 0 8 8"><path d="M1 4l2 2 4-4.5" stroke="#fff" stroke-width="1.5" fill="none"/></svg></span>Access a targeted audience of camping enthusiasts</li>
  </ul>
  <div class="pill abs" style="left:141px;top:1196px;width:127px">Contact Us</div>
  <div class="photo abs" style="left:720px;top:845px;width:339px;height:437px;background:linear-gradient(180deg,#1d47b8 0%,#3c6ad0 30%,#6a5a72 48%,#a0452a 68%,#6e2a14 100%)" role="img" aria-label="Two campers sitting by a campfire beside a tent at dusk"></div>
  <div class="photo-framed abs" style="left:616px;top:1086px;width:227px;height:220px;background:linear-gradient(180deg,#c9cdd2 0%,#9aa7b2 35%,#5f7a4e 60%,#3f6a2c 100%)" role="img" aria-label="Tents pitched on a grassy lakeside campground"></div>
</section>

<section class="features">
  <div class="eyebrow abs" style="left:0;width:1200px;top:82px;justify-content:center"><span class="dash"></span>Our Features<span class="dash"></span></div>
  <h2 class="section-title abs" style="left:0;width:1200px;top:96px;text-align:center">Features of Our Outfitter Directory</h2>
  <div class="feature" style="left:147px;top:170px">
    <svg class="feature-icon" width="64" height="64" viewBox="0 0 64 64"><circle cx="27" cy="27" r="20" stroke="#111" stroke-width="3" fill="none"/><circle cx="27" cy="27" r="14" stroke="#111" stroke-width="1.5" fill="none"/><path d="M18 22a10 10 0 0 1 8-8" stroke="#f65a1c" stroke-width="2.5" fill="none"/><path d="M41 41l16 16" stroke="#111" stroke-width="6" stroke-linecap="round"/></svg>
    <div class="feature-text">Search Functionality To Find Outfitters By Location, Activity, Or Type</div>
  </div>
  <div class="feature" style="left:460px;top:170px">
    <svg class="feature-icon" width="64" height="64" viewBox="0 0 64 64"><rect x="8" y="2" width="48" height="60" rx="4" stroke="#111" stroke-width="3" fill="none"/><circle cx="32" cy="20" r="7" stroke="#111" stroke-width="2.5" fill="none"/><path d="M19 38a13 10 0 0 1 26 0z" stroke="#111" stroke-width="2.5" fill="none"/><path d="M18 47h28M18 54h28" stroke="#f65a1c" stroke-width="3"/></svg>
    <div class="feature-text">Outfitter Profiles With Detailed Information And Reviews</div>
  </div>
  <div class="feature" style="left:774px;top:170px">
    <svg class="feature-icon" width="64" height="64" viewBox="0 0 64 64"><rect x="2" y="8" width="60" height="52" rx="3" stroke="#111" stroke-width="3" fill="none"/><path d="M2 20h60" stroke="#111" stroke-width="3"/><g fill="#111"><rect x="10" y="2" width="4" height="10"/><rect x="22" y="2" width="4" height="10"/><rect x="38" y="2" width="4" height="10"/><rect x="50" y="2" width="4" height="10"/><rect x="9" y="26" width="6" height="5"/><rect x="19" y="26" width="6" height="5"/><rect x="29" y="26" width="6" height="5"/><rect x="39" y="26" width="6" height="5"/><rect x="49" y="26" width="6" height="5"/><rect x="9" y="35" width="6" height="5"/><rect x="19" y="35" width="6" height="5"/><rect x="29" y="35" width="6" height="5"/><rect x="39" y="35" width="6" height="5"/><rect x="9" y="44" width="6" height="5"/><rect x="19" y="44" width="6" height="5"/><rect x="29" y="44" width="6" height="5"/></g><circle cx="51" cy="47" r="7" stroke="#f65a1c" stroke-width="2.5" fill="#fff"/><path d="M47.5 47l2.5 2.5 4-4.5" stroke="#f65a1c" stroke-width="2" fill="none"/></svg>
    <div class="feature-text">Booking System To Make It Easy For Customers To Book Trips</div>
  </div>
  <div class="abs" style="left:0;top:371px;width:1200px;height:396px;background:linear-gradient(180deg,#e1e3e4 0%,#a9b2bb 25%,#7c8a98 45%,#5f7a44 65%,#7b8a38 82%,#4f5a26 100%)" role="img" aria-label="Hiking couple raising trekking poles between two green tents on a mountain meadow"></div>
  <svg class="abs" style="left:0;top:747px" width="1200" height="20" viewBox="0 0 1200 20" preserveAspectRatio="none"><path d="M0 14 Q400 4 800 10 T1200 6 V20 H0 Z" fill="#fff"/></svg>
</section>

<section class="contact">
  <div class="photo abs" style="left:242px;top:2236px;width:338px;height:437px;background:linear-gradient(180deg,#7fa0b8 0%,#9bb3c0 35%,#6c6a4a 52%,#8c7a2a 70%,#4c5a1c 100%)" role="img" aria-label="Camper in a yellow jacket cooking over a small fire beside a tent in a meadow"></div>
  <div class="photo-framed abs" style="left:138px;top:2478px;width:228px;height:220px;background:linear-gradient(180deg,#59683f 0%,#4c7a34 45%,#6e5a44 80%,#5a4a3a 100%)" role="img" aria-label="Person reading inside a green tent in the woods"></div>
  <div class="eyebrow abs" style="left:636px;top:2259px">Quick Inquiry <span class="dash"></span></div>
  <h2 class="section-title abs" style="left:635px;top:2273px">Get in Touch With Us</h2>
  <p class="para abs" style="left:636px;top:2321px;width:430px">Lorem ipsum dolor sit amet, consectetur adipiscing elit, sed do sit em eiusmod tempor incididunt ut labore et dolore magna aliqua.</p>
  <div class="field" style="top:2394px"><div class="fi"><svg width="16" height="16" viewBox="0 0 16 16" fill="none" stroke="#f65a1c" stroke-width="1.2"><circle cx="8" cy="5" r="3.2"/><path d="M2 15a6 5 0 0 1 12 0"/></svg></div><span>Name<b>*</b></span></div>
  <div class="field" style="top:2450px"><div class="fi"><svg width="16" height="16" viewBox="0 0 16 16" fill="none" stroke="#f65a1c" stroke-width="1.2"><rect x="1.5" y="4" width="13" height="10" rx="1"/><path d="M1.5 4.5l6.5 5 6.5-5"/></svg></div><span>Email<b>*</b></span></div>
  <div class="field" style="top:2506px"><div class="fi"><svg width="15" height="15" viewBox="0 0 24 24" fill="none" stroke="#f65a1c" stroke-width="1.8"><path d="M6.6 10.8a15 15 0 0 0 6.6 6.6l2.2-2.2c.3-.3.7-.4 1-.2 1.1.4 2.3.6 3.6.6.6 0 1 .4 1 1V20c0 .6-.4 1-1 1A17 17 0 0 1 3 4c0-.6.4-1 1-1h3.5c.6 0 1 .4 1 1 0 1.3.2 2.5.6 3.6.1.3 0 .7-.2 1z"/></svg></div><span>Phone<b>*</b></span></div>
  <div class="field" style="top:2562px"><div class="fi"><svg width="16" height="16" viewBox="0 0 16 16" fill="none" stroke="#f65a1c" stroke-width="1.2"><circle cx="8" cy="8" r="6.5"/><ellipse cx="8" cy="8" rx="3" ry="6.5"/><path d="M1.5 8h13"/></svg></div><span>Website<b>*</b></span></div>
  <div class="pill abs" style="left:636px;top:2634px;width:126px">Contact Us</div>
</section>

<section class="cta-band">
  <div class="abs" style="inset:0;background:linear-gradient(90deg,#4a5a3c 0%,#5c6a44 35%,#6a7a50 55%,#3f8a8c 75%,#5d6e44 100%)" role="img" aria-label="Two smiling campers lacing their boots in front of a teal tent on a grassy hillside"></div>
  <h2 class="cta-title">Express Interest in<br>Joining Our Directory</h2>
  <div class="pill abs" style="left:142px;top:214px;width:126px;height:36px">Join Now</div>
  <svg class="abs" style="left:0;top:353px" width="1200" height="20" viewBox="0 0 1200 20" preserveAspectRatio="none"><path d="M0 8 Q300 14 600 6 T1200 10 V20 H0 Z" fill="#fff"/></svg>
</section>

<footer>
  <div class="abs" style="left:142px;top:3250px;display:flex;align-items:center;gap:14px">
    <span style="width:44px;height:44px;border-radius:50%;background:var(--orange)"></span>
    <span style="font-weight:700;font-size:24px;line-height:28px;color:var(--navy);width:120px">Hiking Made Simple</span>
  </div>
  <div class="footer-head abs" style="left:526px;top:3212px">CONTACT DETAILS</div>
  <div class="footer-item" style="left:526px;top:3253px"><span class="ring-icon"><svg width="13" height="15" viewBox="0 0 12 15"><path d="M6 0a6 6 0 0 0-6 6c0 4.5 6 9 6 9s6-4.5 6-9a6 6 0 0 0-6-6z" fill="#fff"/><circle cx="6" cy="6" r="2.2" fill="#f65a1c"/></svg></span>123, Building Name, Street<br>City, State XY 123456</div>
  <div class="footer-item" style="left:526px;top:3311px"><span class="ring-icon"><svg width="14" height="11" viewBox="0 0 14 11"><rect x="0.5" y="0.5" width="13" height="10" rx="1.5" fill="none" stroke="#fff" stroke-width="1.2"/><path d="M1 1.5l6 4.5 6-4.5" stroke="#fff" stroke-width="1.2" fill="none"/></svg></span>info@hikingmadesimple.net</div>
  <div class="footer-item" style="left:526px;top:3369px"><span class="ring-icon"><svg width="14" height="14" viewBox="0 0 24 24"><path fill="#fff" d="M6.6 10.8a15 15 0 0 0 6.6 6.6l2.2-2.2c.3-.3.7-.4 1-.2 1.1.4 2.3.6 3.6.6.6 0 1 .4 1 1V20c0 .6-.4 1-1 1A17 17 0 0 1 3 4c0-.6.4-1 1-1h3.5c.6 0 1 .4 1 1 0 1.3.2 2.5.6 3.6.1.3 0 .7-.2 1z"/></svg></span>(555) 318-HIKE</div>
  <div class="footer-head abs" style="left:950px;top:3212px">FOLLOW US</div>
  <div class="footer-item" style="left:950px;top:3244px"><span class="ring-icon"><span class="social-dot"></span></span>Trailbook</div>
  <div class="footer-item" style="left:950px;top:3290px"><span class="ring-icon"><span class="social-dot"></span></span>Chirper</div>
  <div class="footer-item" style="left:950px;top:3337px"><span class="ring-icon"><span class="social-dot"></span></span>Snapgram</div>
  <div class="footer-item" style="left:950px;top:3383px"><span class="ring-icon"><span class="social-dot"></span></span>Linkwork</div>
  <div class="copyright">©2024 Hiking Made Simple. All Rights Reserved.</div>
</footer>

</body>
</html>
```